Criação de Papelaria Profissional para Construção & Engenharia
" Empresa que atua em incorporação imobiliária, administrando a construção de edifícios "

```html
<!DOCTYPE html>
<html lang="pt-BR">
<head>
<meta charset="UTF-8">
<title>Capa Rede Social — Ferraz Lima Engenharia</title>
<link href="https://fonts.googleapis.com/css2?family=Montserrat:wght@500;600;700;800&family=Roboto:wght@400;500;700&display=swap" rel="stylesheet">
<style>
  :root{
    --navy:#1d3a72;
    --ink:#1b2a4a;
    --board-light:#f1f1f1;
    --board-mid:#d9d9d9;
    --panel:#ffffff;
    --line:#dcdde0;
    --side:#eceef1;
    --text:#4b4f56;
    --accent:#5b78b4;
  }
  *{box-sizing:border-box;margin:0;padding:0}
  html,body{width:1200px;height:1200px;overflow:hidden}
  body{
    position:relative;
    background:radial-gradient(circle at 50% 45%,var(--board-light) 0%,#e4e4e4 55%,var(--board-mid) 100%);
    font-family:"Roboto",Arial,sans-serif;
  }
  .frame{
    position:absolute;left:40px;top:40px;width:1120px;height:1120px;
    border:6px solid var(--navy);border-radius:40px;
  }
  .board-title{
    position:absolute;top:18px;left:50%;transform:translateX(-50%);
    padding:6px 40px;background:#ececec;white-space:nowrap;
    font-family:"Montserrat",sans-serif;font-weight:800;font-size:34px;letter-spacing:1px;color:var(--ink);
  }
  .board-logo{
    position:absolute;bottom:20px;left:50%;transform:translateX(-50%);
    display:flex;align-items:center;gap:18px;padding:8px 36px;background:#e2e2e2;white-space:nowrap;
  }
  .mark-square{width:64px;height:64px;background:var(--navy);flex:none}
  .board-logo .name{
    font-family:"Montserrat",sans-serif;font-weight:700;font-size:34px;letter-spacing:3px;color:var(--navy);
  }

  .page{position:absolute;left:84px;top:389px;width:1032px;height:415px;background:var(--panel);box-shadow:0 2px 10px rgba(0,0,0,.18);overflow:hidden}
  .topnav{height:38px;display:flex;align-items:center;border-bottom:1px solid var(--line);font-size:14px;color:var(--text);padding:0 14px;white-space:nowrap}
  .topnav span{margin-right:42px;position:relative}
  .topnav .active{font-weight:700;color:#1d2129}
  .topnav .active::after{content:"";position:absolute;left:0;right:0;bottom:-11px;height:3px;background:var(--navy)}
  .topnav .right{margin-left:auto}
  .topnav .last{margin-right:0}
  .sidebar{position:absolute;left:0;top:38px;width:187px;bottom:0;background:var(--side)}
  .profile{position:absolute;left:5px;top:10px;width:177px;height:187px;background:#fff;border:1px solid var(--line);display:flex;flex-direction:column;align-items:center;justify-content:center;gap:10px}
  .profile .mark-square{width:84px;height:84px}
  .profile .name{font-family:"Montserrat",sans-serif;font-weight:700;font-size:15px;letter-spacing:1px;color:var(--navy)}
  .menu{position:absolute;top:292px;left:0;right:0;font-size:14px;color:var(--text)}
  .menu li{list-style:none;padding:4px 8px;border-bottom:1px solid #d3d6db}
  .menu li:first-child{font-weight:700;color:#1d2129;background:#fff}

  .cover{position:absolute;left:187px;top:38px;width:845px}
  .cover-photo{height:204px;background:linear-gradient(100deg,#2a3d55 0%,#6f8aa8 35%,#c4cfd8 55%,#8a7a5e 80%,#4b3a28 100%)}
  .cover-brand{height:72px;display:flex;align-items:center;justify-content:center;gap:12px}
  .cover-brand .mark-square{width:48px;height:48px}
  .cover-brand .name{font-family:"Montserrat",sans-serif;font-weight:700;font-size:20px;letter-spacing:2px;color:var(--navy)}
  .contact-bar{height:39px;background:var(--navy);display:flex;align-items:center;justify-content:center;gap:60px;color:#fff;font-size:15px;white-space:nowrap}
  .contact-bar .item{display:flex;align-items:center;gap:8px}
  .actions{position:absolute;left:187px;top:362px;right:0;height:36px;display:flex;align-items:center;padding:0 10px;gap:6px}
  .btn{border:1px solid #ccd0d5;background:#f6f7f9;border-radius:2px;font-size:12px;font-weight:700;color:var(--text);padding:5px 9px}
  .btn-send{margin-left:auto;margin-right:10px;width:295px;text-align:center;background:var(--accent);border-color:var(--accent);color:#fff;font-weight:500;font-size:14px}
</style>
</head>
<body>
  <div class="frame"></div>
  <h1 class="board-title">CAPA REDE SOCIAL</h1>

  <main class="page">
    <nav class="topnav">
      <span class="active">Perfil</span>
      <span>Mensagens</span>
      <span>Avisos</span>
      <span>Sobre</span>
      <span>Publicações</span>
      <span class="right">Ajustes</span>
      <span class="last">Ajuda ▾</span>
    </nav>

    <aside class="sidebar">
      <div class="profile"><div class="mark-square"></div><span class="name">FERRAZ LIMA</span></div>
      <ul class="menu"><li>Início</li><li>Sobre</li><li>Fotos</li></ul>
    </aside>

    <section class="cover">
      <div class="cover-photo" role="img" aria-label="Foto de engenheiros com capacetes brancos observando obra de edifícios"></div>
      <div class="cover-brand"><div class="mark-square"></div><span class="name">FERRAZ LIMA</span></div>
      <div class="contact-bar">
        <span class="item">
          <svg width="16" height="16" viewBox="0 0 24 24" fill="#fff"><path d="M6.6 10.8a15 15 0 0 0 6.6 6.6l2.2-2.2a1 1 0 0 1 1-.25 11.4 11.4 0 0 0 3.6.6 1 1 0 0 1 1 1V20a1 1 0 0 1-1 1A17 17 0 0 1 3 4a1 1 0 0 1 1-1h3.5a1 1 0 0 1 1 1c0 1.25.2 2.45.6 3.6a1 1 0 0 1-.25 1z"/></svg>
          (12) 9700-4512</span>
        <span class="item">
          <svg width="18" height="14" viewBox="0 0 18 14" fill="none" stroke="#fff" stroke-width="1.6"><rect x="1" y="1" width="16" height="12"/><path d="M1 1l8 7 8-7"/></svg>
          contato@ferrazlima.com.br</span>
        <span class="item">
          <svg width="14" height="18" viewBox="0 0 14 18" fill="none" stroke="#fff" stroke-width="1.6"><path d="M7 17s6-6.2 6-10A6 6 0 0 0 1 7c0 3.8 6 10 6 10z"/><circle cx="7" cy="7" r="2"/></svg>
          R. Alameda Serra, 48 Ubatuba SP</span>
      </div>
    </section>

    <div class="actions">
      <span class="btn">Seguir ▾</span>
      <span class="btn">Salvar ▾</span>
      <span class="btn">↗ Enviar</span>
      <span class="btn">···</span>
      <span class="btn btn-send">Contato ✎</span>
    </div>
  </main>

  <footer class="board-logo"><div class="mark-square"></div><span class="name">FERRAZ LIMA</span></footer>
</body>
</html>
```